Military / Law Enforcement / Security Industry sales company needing a website redesign

Stonewren Supply is a leading US sales company in the Military, Law Enforcement, and security industries. We have been in business for 15 yrs and are based in the US. We are looking for an updated redesign of our company's website. We are interested in a sleek, modern, and dynamic design that represents our company and the high end products that we offer. Please visit our current website at www.stonewrensupply.com. This website was developed for us about 7 yrs ago and has not undergone any major changes since then.

```html
<!DOCTYPE html>
<html lang="en">
<head>
<meta charset="utf-8">
<title>Stonewren Supply</title>
<link rel="stylesheet" href="https://fonts.googleapis.com/css2?family=Oswald:wght@400;500;700&family=Roboto:wght@400;500&display=swap">
<style>
:root{
  --orange:#f04a1d;
  --ink:#141414;
  --dark:#1c1c1c;
  --dark-2:#262626;
  --grey:#8a8a8a;
  --line:#e4e4e4;
  --paper:#ffffff;
  --soft:#f3f3f3;
}
*{margin:0;padding:0;box-sizing:border-box}
html,body{width:1200px;height:2636px;overflow:hidden;background:var(--paper)}
body{font-family:"Roboto",Arial,sans-serif;color:var(--ink);position:relative}
.abs{position:absolute}
.display{font-family:"Oswald","Arial Narrow",sans-serif;font-weight:700;text-transform:uppercase;letter-spacing:.5px}
.eyebrow{font-family:"Oswald",sans-serif;font-weight:500;font-size:11px;letter-spacing:1.5px;color:var(--orange);text-transform:uppercase}
.small{font-size:11px;color:var(--grey);line-height:1.6}
.btn{display:inline-block;font-family:"Oswald",sans-serif;font-weight:500;font-size:11px;letter-spacing:1px;text-transform:uppercase;color:#fff;padding:11px 22px}
.btn-dark{background:var(--ink)}
.btn-orange{background:var(--orange)}
.cross{width:22px;height:22px}

/* featured strip */
.feature-card{top:0;width:256px;height:250px;background:var(--paper)}
.feature-card .photo{width:100%;height:100%}
.feature-card.alt{background:var(--soft)}
.sale-badge{top:14px;left:14px;background:var(--orange);color:#fff;font-size:9px;padding:3px 7px;font-family:"Oswald",sans-serif}
.feature-name{font-family:"Oswald",sans-serif;font-weight:500;font-size:12px;text-transform:uppercase}
.price{font-size:11px;color:var(--grey);margin-top:4px}

/* hero */
.hero-soldier{left:220px;top:360px;width:300px;height:560px;background:linear-gradient(180deg,#5c5a4c,#3b3a33 60%,#2b2a26)}
.hero-knives{left:400px;top:640px;width:200px;height:260px;background:linear-gradient(160deg,#3a3a3a,#1d1d1d)}
.hero-copy{left:660px;top:540px;width:330px}
.hero-copy h1{font-size:34px;line-height:1.15;margin:12px 0 16px}

/* stats */
.stats{top:960px;left:0;width:1200px;height:150px;border-top:1px solid var(--line);border-bottom:1px solid var(--line)}
.stat{top:40px;width:200px;text-align:center}
.stat .label{font-size:10px;color:var(--grey);text-transform:uppercase;letter-spacing:1px}
.stat .num{font-family:"Oswald",sans-serif;font-weight:700;font-size:34px;margin-top:6px}

/* banner */
.banner{top:1124px;left:0;width:1200px;height:420px;background:linear-gradient(90deg,#2a2622 0%,#4a4238 45%,#6e6a62 75%,#3f3b35 100%)}
.banner-copy{left:192px;top:150px;width:380px;color:#fff}
.banner-copy h2{font-size:32px;line-height:1.15;margin:10px 0 22px}

/* service bar */
.services{top:1544px;left:0;width:1200px;height:116px;background:var(--dark)}
.service{top:38px;width:200px;display:flex;gap:12px;align-items:flex-start}
.service .t{font-family:"Oswald",sans-serif;font-size:11px;color:#fff;text-transform:uppercase;letter-spacing:.5px}
.service .d{font-size:10px;color:#9a9a9a;margin-top:4px}

/* top products */
.section-head{top:1716px;left:0;width:1200px;text-align:center}
.section-head h2{font-size:30px;margin-top:8px}
.product{top:1812px;width:190px}
.product .photo{height:190px;background:linear-gradient(180deg,#f7f7f7,#ebebeb)}
.product .name{font-family:"Oswald",sans-serif;font-weight:500;font-size:11px;text-transform:uppercase;margin-top:14px}
.stars{color:var(--orange);font-size:11px;letter-spacing:1px;margin-top:4px}

/* newsletter */
.newsletter{top:2110px;left:192px;width:816px}
.newsletter h2{font-size:24px;margin-top:8px}
.email-field{left:450px;top:16px;width:366px;border-bottom:1px solid #cfcfcf;padding-bottom:10px;font-size:11px;color:var(--grey)}
.consent{left:450px;top:58px;font-size:10px;color:var(--grey);display:flex;gap:8px;align-items:center}
.box{width:10px;height:10px;border:1px solid #bdbdbd;display:inline-block}

/* footer */
.footer{top:2260px;left:0;width:1200px;height:376px;background:var(--dark);color:#cfcfcf}
.brand{left:192px;top:50px;font-family:"Oswald",sans-serif;font-weight:700;font-size:20px;color:#fff;text-transform:uppercase;display:flex;gap:10px;align-items:center}
.brand .sq{width:18px;height:18px;background:#fff}
.col-title{font-family:"Oswald",sans-serif;font-weight:500;font-size:11px;color:#fff;text-transform:uppercase;letter-spacing:1px}
.links li{list-style:none;font-size:11px;color:#bdbdbd;line-height:1.9}
.mini{display:flex;gap:10px;margin-top:16px}
.mini .thumb{width:44px;height:44px;background:linear-gradient(160deg,#3a3a3a,#232323)}
.mini .n{font-family:"Oswald",sans-serif;font-size:10px;color:#fff;text-transform:uppercase}
.social{width:22px;height:22px;border-radius:50%;background:var(--dark-2);display:inline-block;margin-right:6px}
.copyright{left:192px;top:346px;font-size:10px;color:#8a8a8a}
</style>
</head>
<body>

<!-- featured strip -->
<div class="abs feature-card" style="left:192px"><div class="photo" role="img" aria-label="Black tactical bulletproof vest" style="background:radial-gradient(circle at 50% 45%,#3a3a3a 0 28%,#fff 29%)"></div></div>
<div class="abs feature-card alt" style="left:472px"><div class="photo" role="img" aria-label="Compact submachine pistol" style="background:radial-gradient(ellipse 34% 18% at 50% 48%,#2b2b2b 0 95%,transparent 100%)"></div></div>
<div class="abs feature-card" style="left:752px"><div class="photo" role="img" aria-label="Automatic rifle" style="background:radial-gradient(ellipse 40% 12% at 50% 48%,#2e2e2e 0 95%,transparent 100%)"></div><span class="abs sale-badge">SALE</span></div>
<div class="abs" style="left:192px;top:276px"><div class="feature-name">Bulletproof vest</div><div class="price">$129.00</div></div>
<div class="abs" style="left:472px;top:276px"><div class="feature-name">Laser pistol 9mm</div><div class="price">$84.00</div></div>
<div class="abs" style="left:752px;top:276px"><div class="feature-name">Range gun automatic rifle</div><div class="price">$210.00</div></div>

<!-- hero -->
<div class="abs hero-soldier" role="img" aria-label="Soldier in full tactical gear holding a rifle"></div>
<div class="abs hero-knives" role="img" aria-label="Tactical knives and ammunition on a dark surface"></div>
<div class="abs hero-copy">
  <div class="eyebrow">Best in style</div>
  <h1 class="display">The widest selection of weapons and gear for purchase</h1>
  <p class="small">Gear for professionals, trusted by those who serve and protect every single day.</p>
  <a class="btn btn-dark" style="margin-top:20px">View all products</a>
</div>
<svg class="abs cross" style="left:1060px;top:400px" viewBox="0 0 22 22"><path d="M11 2v18M2 11h18" stroke="#d8d8d8" stroke-width="1.5"/></svg>
<svg class="abs cross" style="left:1100px;top:400px" viewBox="0 0 22 22"><path d="M11 2v18M2 11h18" stroke="#d8d8d8" stroke-width="1.5"/></svg>
<svg class="abs cross" style="left:690px;top:400px" viewBox="0 0 22 22"><path d="M11 2v18M2 11h18" stroke="#d8d8d8" stroke-width="1.5"/></svg>

<!-- stats -->
<div class="abs stats">
  <div class="abs stat" style="left:230px"><div class="label">Items</div><div class="num">2548</div></div>
  <div class="abs stat" style="left:500px"><div class="label">Years</div><div class="num">15+</div></div>
  <div class="abs stat" style="left:780px"><div class="label">Brands</div><div class="num">256</div></div>
  <svg class="abs cross" style="left:100px;top:64px" viewBox="0 0 22 22"><path d="M11 2v18M2 11h18" stroke="#d8d8d8" stroke-width="1.5"/></svg>
  <svg class="abs cross" style="left:1070px;top:64px" viewBox="0 0 22 22"><path d="M11 2v18M2 11h18" stroke="#d8d8d8" stroke-width="1.5"/></svg>
</div>

<!-- banner -->
<div class="abs banner" role="img" aria-label="Shooter in sunglasses aiming a rifle with optic sight">
  <div class="abs banner-copy">
    <div class="eyebrow">Holiday season</div>
    <h2 class="display">Perfect holiday gifts for enthusiasts and pros</h2>
    <a class="btn btn-orange">Shop collections</a>
  </div>
</div>

<!-- services -->
<div class="abs services">
  <div class="abs service" style="left:192px"><svg width="24" height="20" viewBox="0 0 24 20"><path d="M1 3h14v11H1zM15 7h5l3 4v3h-8z" fill="none" stroke="#f04a1d" stroke-width="1.5"/></svg><div><div class="t">Nationwide shipping</div><div class="d">Fast delivery</div></div></div>
  <div class="abs service" style="left:420px"><svg width="24" height="20" viewBox="0 0 24 20"><rect x="1" y="3" width="22" height="14" fill="none" stroke="#f04a1d" stroke-width="1.5"/><path d="M1 8h22" stroke="#f04a1d" stroke-width="1.5"/></svg><div><div class="t">Secure paying</div><div class="d">Safe checkout</div></div></div>
  <div class="abs service" style="left:640px"><svg width="24" height="20" viewBox="0 0 24 20"><path d="M12 1l9 4v6c0 4-4 7-9 8-5-1-9-4-9-8V5z" fill="none" stroke="#f04a1d" stroke-width="1.5"/></svg><div><div class="t">Buyer protection</div><div class="d">Full coverage</div></div></div>
  <div class="abs service" style="left:860px"><svg width="24" height="20" viewBox="0 0 24 20"><path d="M3 10a9 9 0 0 1 18 0M3 10v5h3v-5zM21 10v5h-3v-5z" fill="none" stroke="#f04a1d" stroke-width="1.5"/></svg><div><div class="t">Secure support</div><div class="d">Always here</div></div></div>
</div>

<!-- top products -->
<div class="abs section-head"><div class="eyebrow">Hot deals</div><h2 class="display">Top products</h2></div>
<div class="abs product" style="left:192px"><div class="photo" role="img" aria-label="Semi-automatic pistol"></div><div class="name">Steel gun automatic pistol</div><div class="stars">★★★★★</div><div class="price">$58.00</div></div>
<div class="abs product" style="left:404px"><div class="photo" role="img" aria-label="Rifle buttstock"></div><div class="name">AR rifle buttstock</div><div class="stars">★★★★★</div><div class="price">$42.00</div></div>
<div class="abs product" style="left:616px"><div class="photo" role="img" aria-label="Black handgun"></div><div class="name">9mm pistol, no rounds</div><div class="stars">★★★★★</div><div class="price">$96.00</div></div>
<div class="abs product" style="left:828px"><div class="photo" role="img" aria-label="Rifle with mounted scope"></div><div class="name">5.56mm rifle, long scope</div><div class="stars">★★★★★</div><div class="price">$240.00</div></div>

<!-- newsletter -->
<div class="abs newsletter">
  <div class="eyebrow">Newsletter sign up</div>
  <h2 class="display">Enter your email address</h2>
  <div class="abs email-field">Type your email here<svg class="abs" style="right:0;top:2px" width="22" height="10" viewBox="0 0 22 10"><path d="M0 5h20M16 1l4 4-4 4" fill="none" stroke="#141414" stroke-width="1.4"/></svg></div>
  <div class="abs consent"><span class="box"></span>I agree to the Privacy Policy</div>
</div>

<!-- footer -->
<div class="abs footer">
  <div class="abs brand"><span class="sq"></span>Stonewren Supply</div>
  <p class="abs small" style="left:192px;top:96px;width:220px;color:#a8a8a8">We are your online store, trusted supplier for law enforcement and security pros.</p>
  <div class="abs" style="left:192px;top:160px;width:220px;border-bottom:1px solid #444;padding-bottom:8px;font-size:10px;color:#a8a8a8">Enter Your Email Address</div>
  <div class="abs" style="left:192px;top:196px;font-size:10px;color:#8a8a8a;display:flex;gap:8px;align-items:center"><span class="box" style="border-color:#555"></span>I agree to the Privacy Policy</div>

  <div class="abs" style="left:468px;top:40px;width:180px">
    <div class="col-title">Best sellers</div>
    <div class="mini"><div class="thumb" role="img" aria-label="Pistol"></div><div><div class="n">Steel gun automatic</div><div class="stars">★★★★★</div><div class="price" style="color:#a8a8a8">$58.00</div></div></div>
    <div class="mini"><div class="thumb" role="img" aria-label="Rifle"></div><div><div class="n">9mm rifle, no rounds</div><div class="stars">★★★★★</div><div class="price" style="color:#a8a8a8">$96.00</div></div></div>
  </div>

  <div class="abs" style="left:690px;top:40px">
    <div class="col-title">Links</div>
    <ul class="links" style="margin-top:10px"><li>Home</li><li>Services</li><li>About Us</li><li>Shop</li><li>Contact</li></ul>
  </div>

  <div class="abs" style="left:820px;top:40px">
    <div class="col-title">Socials</div>
    <div style="margin-top:12px"><span class="social"></span><span class="social"></span><span class="social"></span><span class="social"></span></div>
  </div>

  <div class="abs copyright">© Stonewren Supply 2024. All rights reserved.</div>
</div>

</body>
</html>
```